Form With Tamsin - Health and Wellness Business Card and Logo

I need a business card design with a logo for my business you can check out at www.formwithtamsin.net. I want something more original, simplistic, and memorable than the basic logo I have on my site currently. I am a health and wellness coach and I offer mindset coaching and nutrition plans. I like the colour teal and dark grey/black for my theme colours. I emphasize growth, longterm change, and the whole package of "healthy mind, healthy body, healthy life". I had played around the idea of intertwining 3 T's or incorporating growth (leaves etc.) into my design. I want my expertise and experience to show through. In one glance I want people to understand with confidence I can help them accomplish anything they set their minds to. I look forward to seeing what everyone comes up with!

Industry/Entity Type

Health And Wellness

Contact Information for Business Card

Form With Tamsin
Tamsin Arlow
BSc, Health & Wellness Coach
"Manifest your best"
www.formwithtamsin.net
formwithtamsin@mailo.example
613-472-9186
[Instagram logo] @tamsinarlow

Colors
33b8a4
ffffff
333333
000000

Requirements
Must have
• A memorable and unique logo for my business!
Nice to have
• Could have the phrase "Are you unhappy with your body and state of health?" or "It takes the right skills to develop habits in order to create long term change. I can help you get there."

```html
<!DOCTYPE html>
<html lang="en">
<head>
<meta charset="utf-8">
<title>Form With Tamsin – Business Card and Mobile Page</title>
<link rel="stylesheet" href="https://fonts.googleapis.com/css2?family=Roboto+Slab:wght@600&family=Roboto+Condensed:wght@300;400&family=Dancing+Script:wght@500&family=Montserrat:ital,wght@0,400;0,600;1,800&family=Raleway:wght@400;700&display=swap">
<style>
  :root {
    --teal-deep: #127e80;
    --teal-light: #22a094;
    --teal-bright: #33b8a4;
    --script-cyan: #4fe6e6;
    --white: #ffffff;
    --ink: #000000;
    --charcoal: #333333;
    --backdrop: #ecefee;
    --photo-top: #8fb8a0;
    --photo-bottom: #3c4a44;
    --leaf-grey: #9a9a9a;
  }
  * { box-sizing: border-box; margin: 0; padding: 0; }
  html, body { width: 1200px; height: 799px; overflow: hidden; }
  body { background: var(--backdrop); position: relative; font-family: "Montserrat", sans-serif; }

  /* Mobile landing page */
  .mobile-page {
    position: absolute; left: 70px; top: 120px; width: 290px; height: 560px;
    background: var(--white); border-radius: 6px;
    display: flex; flex-direction: column; align-items: center;
    padding: 38px 26px 0; text-align: center;
  }
  .mobile-page__icon { width: 54px; height: 54px; background: var(--leaf-grey); border-radius: 50%; }
  .mobile-page__headline {
    margin-top: 16px; font-family: "Raleway", sans-serif; font-weight: 700;
    font-size: 20px; color: var(--ink); letter-spacing: 0.2px;
  }
  .mobile-page__photo {
    margin-top: 12px; width: 170px; height: 178px;
    background: linear-gradient(180deg, var(--photo-top), var(--photo-bottom));
  }
  .mobile-page__copy {
    margin-top: 14px; font-family: "Raleway", sans-serif; font-size: 14.5px;
    line-height: 1.35; color: var(--charcoal);
  }
  .mobile-page__cta {
    margin-top: 16px; font-family: "Raleway", sans-serif; font-weight: 700;
    font-size: 15px; color: var(--ink);
  }

  /* Business cards */
  .card {
    position: absolute; width: 590px; height: 330px;
    background: linear-gradient(180deg, var(--teal-deep), var(--teal-light));
    color: var(--white);
  }
  .card--front { left: 450px; top: 60px; }
  .card--back { left: 560px; top: 420px; }

  .brand-mark {
    position: absolute; border: 1.5px solid var(--white); border-radius: 50%;
    display: flex; align-items: center; justify-content: center;
    font-family: "Montserrat", sans-serif; font-weight: 400; color: var(--white);
    text-align: center;
  }
  .card--front .brand-mark { left: 58px; top: 32px; width: 98px; height: 98px; font-size: 10px; }
  .card--back .brand-mark {
    left: 50%; top: 50%; width: 154px; height: 154px; transform: translate(-50%, -50%);
    font-size: 15px;
  }

  .card__identity { position: absolute; left: 270px; top: 88px; width: 240px; text-align: center; }
  .card__name { font-family: "Roboto Slab", serif; font-weight: 600; font-size: 18px; letter-spacing: 0.3px; }
  .card__title { margin-top: 3px; font-family: "Roboto Condensed", sans-serif; font-weight: 300; font-size: 12.5px; }
  .card__tagline {
    display: inline-block; margin-top: 10px; padding: 4px 12px;
    background: var(--ink); border-radius: 6px;
    font-family: "Montserrat", sans-serif; font-style: italic; font-weight: 800;
    font-size: 12.5px; letter-spacing: 0.6px; color: var(--white);
  }

  .card__question {
    position: absolute; left: 28px; top: 165px; width: 170px; text-align: center;
    font-family: "Dancing Script", cursive; font-weight: 500; font-size: 17px;
    line-height: 1.12; color: var(--script-cyan);
  }

  .card__contacts { position: absolute; left: 262px; top: 190px; list-style: none; }
  .contact-line {
    display: flex; align-items: center; gap: 8px; margin-bottom: 12px;
    font-family: "Montserrat", sans-serif; font-size: 10.5px; letter-spacing: 0.4px;
    text-transform: uppercase;
  }
  .contact-line svg { width: 16px; height: 16px; flex: none; }
  .contact-line__square { width: 14px; height: 14px; margin: 0 1px; background: var(--white); border-radius: 3px; flex: none; }
</style>
</head>
<body>

  <section class="mobile-page" aria-label="Mobile landing page">
    <div class="mobile-page__icon" role="img" aria-label="Growth leaf emblem"></div>
    <h1 class="mobile-page__headline">MANIFEST YOUR BEST!</h1>
    <div class="mobile-page__photo" role="img" aria-label="Photo of the coach outdoors flexing her arm"></div>
    <p class="mobile-page__copy">It takes the right skills to develop habits in order to create long term change.</p>
    <p class="mobile-page__cta">I can help you get there.</p>
  </section>

  <article class="card card--front" aria-label="Business card front">
    <div class="brand-mark">Form With Tamsin</div>

    <div class="card__identity">
      <h2 class="card__name">Tamsin Arlow</h2>
      <p class="card__title">BSc, Health &amp; Wellness Coach</p>
      <p class="card__tagline">MANIFEST YOUR BEST</p>
    </div>

    <p class="card__question">Are you unhappy<br>with your body<br>and state of health?</p>

    <ul class="card__contacts">
      <li class="contact-line">
        <svg viewBox="0 0 16 16" aria-hidden="true" fill="none" stroke="currentColor" stroke-width="1.1">
          <circle cx="8" cy="8" r="7.2"/>
          <path d="M4.5 8 L8 5 L11.5 8 M5.5 7.3 V11 H10.5 V7.3"/>
        </svg>
        www.formwithtamsin.net
      </li>
      <li class="contact-line">
        <svg viewBox="0 0 16 16" aria-hidden="true" fill="none" stroke="currentColor" stroke-width="1.1">
          <circle cx="8" cy="8" r="7.2"/>
          <rect x="4.3" y="5.3" width="7.4" height="5.4"/>
          <path d="M4.3 5.3 L8 8.3 L11.7 5.3"/>
        </svg>
        formwithtamsin@mailo.example
      </li>
      <li class="contact-line">
        <span class="contact-line__square" aria-hidden="true"></span>
        @tamsinarlow
      </li>
    </ul>
  </article>

  <article class="card card--back" aria-label="Business card back">
    <div class="brand-mark">Form With Tamsin</div>
  </article>

</body>
</html>
```